Have photos and logo just need help with web banner

Dimensions: 950 width by 425 height, pixels
Resolution: 92 DPI
Layout: Landscape
Format: JPG

Target Market(s)

Luxury market for women 28-55

Industry/Entity Type

Landscape

Number of Pages Required

1 page

Font styles to use
Script

Requirements
Must have
• Elegant, sophisticated feel
• Tagline: bags with a silver lining
Nice to have
• Shoes bag / has athletic, strong feel
Should not have
• Not cluttered. Not confusing.

```html
<!DOCTYPE html>
<html lang="en">
<head>
<meta charset="utf-8">
<title>Bags with a silver lining – web banner</title>
<link rel="stylesheet" href="https://fonts.googleapis.com/css2?family=Fondamento&display=swap">
<style>
  :root {
    --silver-light: #f4f4f2;
    --silver-mid: #c9c9c6;
    --silver-deep: #8f8f8c;
    --text-white: #ffffff;
    --text-shadow: rgba(40, 40, 40, 0.75);
    --logo-bg: #ffffff;
    --logo-ink: #111111;
    --photo-station: #4a4640;
    --photo-ring: #5a6a86;
    --photo-bag: #8a8a8a;
  }
  html, body {
    margin: 0;
    padding: 0;
    width: 1200px;
    height: 537px;
    overflow: hidden;
    background: #ffffff;
  }
  .banner {
    position: relative;
    width: 1200px;
    height: 537px;
    overflow: hidden;
    font-family: "Fondamento", cursive;
  }
  .fabric-backdrop {
    position: absolute;
    inset: 0;
    background:
      radial-gradient(ellipse 420px 260px at 540px 120px, rgba(255,255,255,0.9), transparent 70%),
      radial-gradient(ellipse 380px 220px at 980px 420px, rgba(255,255,255,0.7), transparent 70%),
      linear-gradient(125deg, var(--silver-mid) 0%, var(--silver-light) 30%, var(--silver-mid) 55%, var(--silver-light) 75%, var(--silver-deep) 100%);
  }
  .headline {
    position: absolute;
    margin: 0;
    color: var(--text-white);
    font-weight: 400;
    text-shadow: 3px 4px 5px var(--text-shadow);
    line-height: 1;
    white-space: nowrap;
  }
  .headline--top {
    left: 64px;
    top: 30px;
    font-size: 86px;
  }
  .headline--bottom {
    left: 62px;
    top: 392px;
    font-size: 92px;
  }
  .photo-strip {
    position: absolute;
    left: 61px;
    top: 183px;
    display: flex;
    gap: 3px;
  }
  .photo {
    width: 225px;
    height: 167px;
  }
  .photo--station { background: linear-gradient(180deg, #2b2a28 0%, var(--photo-station) 55%, #b59f73 100%); }
  .photo--ring { background: linear-gradient(180deg, #3a4a6a 0%, var(--photo-ring) 50%, #2d3440 100%); }
  .photo--bag { background: linear-gradient(180deg, #b8b6b0 0%, var(--photo-bag) 60%, #3a3a3a 100%); }
  .brand-box {
    position: absolute;
    right: 0;
    top: 0;
    width: 274px;
    height: 244px;
    background: var(--logo-bg);
    display: flex;
    align-items: center;
    justify-content: center;
  }
  .brand-name {
    font-family: "Fondamento", cursive;
    font-size: 32px;
    letter-spacing: 7px;
    color: var(--logo-ink);
    margin-left: 7px;
    white-space: nowrap;
  }
</style>
</head>
<body>
  <div class="banner">
    <div class="fabric-backdrop" role="img" aria-label="Close-up of glossy silver bag lining with a brass zipper"></div>

    <h1 class="headline headline--top">bags</h1>

    <div class="photo-strip">
      <div class="photo photo--station" role="img" aria-label="Black bag resting on a bench in a subway station"></div>
      <div class="photo photo--ring" role="img" aria-label="Boxers sparring in a boxing ring"></div>
      <div class="photo photo--bag" role="img" aria-label="Open bag with silver lining holding boxing gloves and a laptop"></div>
    </div>

    <p class="headline headline--bottom">with a silver lining</p>

    <div class="brand-box">
      <span class="brand-name">ZALVIRE</span>
    </div>
  </div>
</body>
</html>
```